Business card

I need a business card design for my consulting company in animal welfare for livestock. I like clean, crisp, simple.

One I imagined was double-sided:
side1: just my name and contact information
side2: silhouette of farm animals. Could be 3 (pig, cow, chicken) or all the species (pig, cow, chicken, duck, sheep, rabbit, etc) that continue the length of the card. I have attached an image of a silhouette style.

But, I am open to any concept.

```html
<!DOCTYPE html>
<html lang="en">
<head>
<meta charset="utf-8">
<title>Business Card – Maren Holloway</title>
<link href="https://fonts.googleapis.com/css2?family=Open+Sans:wght@400;600;700&display=swap" rel="stylesheet">
<style>
  :root {
    --page-bg: #ffffff;
    --card-white: #ffffff;
    --brand-green: #4fa845;
    --rule-green: #6cbf5c;
    --green-light: #68bd58;
    --green-mid: #3f9142;
    --green-dark: #23672f;
    --ink-dark: #2f2f2f;
    --ink-soft: #555555;
    --card-shadow: 0 2px 5px rgba(0, 0, 0, 0.28);
  }
  * { margin: 0; padding: 0; box-sizing: border-box; }
  html, body {
    width: 1200px;
    height: 1000px;
    overflow: hidden;
    background: var(--page-bg);
    font-family: "Open Sans", Arial, sans-serif;
  }
  .canvas {
    position: relative;
    width: 1200px;
    height: 1000px;
  }
  .card {
    position: absolute;
    top: 344px;
    width: 520px;
    height: 312px;
    box-shadow: var(--card-shadow);
    overflow: hidden;
  }
  .card--front {
    left: 53px;
    background: var(--card-white);
    border: 1px solid #e2e2e2;
  }
  .card--back {
    left: 627px;
    background: radial-gradient(ellipse 75% 95% at 36% 45%,
      var(--green-light) 0%, var(--green-mid) 55%, var(--green-dark) 100%);
  }
  .holder-name {
    position: absolute;
    left: 40px;
    top: 150px;
    font-size: 21px;
    font-weight: 700;
    color: var(--brand-green);
    letter-spacing: 0.2px;
  }
  .holder-tagline {
    position: absolute;
    left: 40px;
    top: 184px;
    font-size: 14.5px;
    font-weight: 600;
    color: var(--ink-dark);
    letter-spacing: 0.3px;
  }
  .divider {
    position: absolute;
    left: 40px;
    right: 0;
    top: 222px;
    height: 1px;
    background: var(--rule-green);
  }
  .contact-list {
    position: absolute;
    left: 40px;
    top: 238px;
    list-style: none;
    font-size: 13.5px;
    line-height: 22px;
  }
  .contact-label {
    color: var(--ink-dark);
    margin-right: 8px;
    letter-spacing: 0.3px;
  }
  .contact-value {
    color: var(--ink-soft);
    letter-spacing: 1px;
  }
  .animal-row {
    position: absolute;
    left: 31px;
    top: 213px;
    width: 460px;
    height: 80px;
    border-radius: 6px;
    background: linear-gradient(90deg, rgba(255,255,255,0.16), rgba(255,255,255,0.26));
  }
</style>
</head>
<body>
  <main class="canvas">
    <section class="card card--front" aria-label="Card front">
      <h1 class="holder-name">Maren Holloway</h1>
      <p class="holder-tagline">Welfare Services for Livestock Stakeholders</p>
      <div class="divider"></div>
      <ul class="contact-list">
        <li><span class="contact-label">Email.</span><span class="contact-value">maren.holloway@example.com</span></li>
        <li><span class="contact-label">Phone.</span><span class="contact-value">+1.555.010.2746</span></li>
      </ul>
    </section>

    <section class="card card--back" aria-label="Card back">
      <div class="animal-row" role="img" aria-label="White silhouettes of farm animals in a row growing in size: duck, chicken, sheep, pig and cow"></div>
    </section>
  </main>
</body>
</html>
```